Quill|Marlow & Petrie business card contest

We need a logo for an upscale boutique diversified company involved in real estate, investments, cattle, and more. Our businesses DO NOT need to be reflected in the business card nor do we want them noted. This is our logo and colors and we love our logo and colors. Our logo looks best against a black background and we like to include the firm name in our logo usage. importantly, the names Quill and Marlow are separated by | not / and we use an ampersand not the word and.
On the front of the card, we want to include:
company logo and name (Quill|Marlow & Petrie)
on the back, we would definitely include:
address, email, cell #
logo and name (smaller size than front)

The variable will be location of individual name and title (mine for example is ) - whether on the front OR on the back. interested in variations from which to choose
Dr. Owen T. Caldecott, CFA
Scientifique des Fusées Financières

we would like to use contemporary symbols for address, email address, cell # with an option for web site that we do not intend to use initially. we like two sided cards and believe this design should use four rounded corners with the standard size. we prefer thicker card stock and may look at metal.

```html
<!DOCTYPE html>
<html lang="en">
<head>
<meta charset="utf-8">
<title>Quill|Marlow &amp; Petrie — Business Card</title>
<link rel="stylesheet" href="https://fonts.googleapis.com/css2?family=Roboto:wght@400;700&display=swap">
<style>
  :root {
    --card-white: #ffffff;
    --brand-orange: #e78224;
    --brand-grey: #656565;
    --card-edge: #e3c9a8;
    --ink-light: #ffffff;
    --page-bg: #ffffff;
  }
  * { box-sizing: border-box; margin: 0; padding: 0; }
  html, body {
    width: 1200px; height: 720px; overflow: hidden;
    background: var(--page-bg);
    font-family: "Roboto", Arial, sans-serif;
  }
  .business-card {
    position: relative;
    width: 1200px; height: 720px;
    border-radius: 32px;
    border: 1.5px solid var(--card-edge);
    overflow: hidden;
    background: var(--card-white);
  }
  .brand-panel {
    position: absolute; left: 0; top: 0;
    width: 564px; height: 100%;
    background: var(--card-white);
  }
  .brand-name {
    position: absolute; left: 0; width: 622px; top: 400px;
    text-align: center;
    font-size: 38px; font-weight: 400;
    color: var(--brand-grey);
    letter-spacing: 0.5px;
    white-space: nowrap;
  }
  .contact-panel {
    position: absolute; left: 564px; top: 0; right: 0; height: 100%;
    background: var(--brand-orange);
  }
  .panel-divider {
    position: absolute; left: 30px; top: 160px;
    width: 6px; height: 400px;
    background: linear-gradient(to right, rgba(0,0,0,0.28), rgba(0,0,0,0));
    filter: blur(1.5px);
  }
  .person-name {
    position: absolute; left: 52px; top: 186px;
    font-size: 39px; font-weight: 700;
    color: var(--ink-light);
    white-space: nowrap;
  }
  .person-title {
    position: absolute; left: 52px; top: 236px;
    font-size: 26px; font-weight: 400;
    color: var(--ink-light);
    white-space: nowrap;
  }
  .contact-list {
    position: absolute; left: 45px; top: 335px;
    list-style: none;
  }
  .contact-item {
    display: flex; align-items: center;
    height: 37px; margin-bottom: 16.5px;
    font-size: 27px; color: var(--ink-light);
    white-space: nowrap;
  }
  .contact-icon {
    width: 37px; height: 37px; margin-right: 6px; flex: none;
  }
  .contact-icon .disc { fill: var(--ink-light); }
  .contact-icon .glyph { fill: var(--brand-orange); }
  .contact-icon .glyph-line { fill: none; stroke: var(--brand-orange); stroke-width: 1.8; }
</style>
</head>
<body>
  <div class="business-card">
    <section class="brand-panel">
      <p class="brand-name">Quill|Marlow &amp; Petrie</p>
    </section>

    <section class="contact-panel">
      <div class="panel-divider"></div>
      <h1 class="person-name">Dr. Owen T. Caldecott, CFA</h1>
      <p class="person-title">Scientifique Des Fusées Financières</p>

      <ul class="contact-list">
        <li class="contact-item">
          <svg class="contact-icon" viewBox="0 0 36 36" aria-hidden="true">
            <circle class="disc" cx="18" cy="18" r="18"/>
            <rect class="glyph-line" x="12.5" y="8.5" width="11" height="19" rx="2"/>
            <rect class="glyph" x="15.5" y="23.5" width="5" height="1.8" rx="0.9"/>
          </svg>
          <span>555 018 2746</span>
        </li>
        <li class="contact-item">
          <svg class="contact-icon" viewBox="0 0 36 36" aria-hidden="true">
            <circle class="disc" cx="18" cy="18" r="18"/>
            <rect class="glyph" x="9" y="12" width="18" height="13" rx="1.5"/>
            <path d="M9.5 12.8 L18 19.5 L26.5 12.8" fill="none" stroke="#ffffff" stroke-width="1.6"/>
          </svg>
          <span>owen@qmpetrie.com</span>
        </li>
        <li class="contact-item">
          <svg class="contact-icon" viewBox="0 0 36 36" aria-hidden="true">
            <circle class="disc" cx="18" cy="18" r="18"/>
            <circle class="glyph-line" cx="18" cy="18" r="10"/>
            <ellipse class="glyph-line" cx="18" cy="18" rx="4.5" ry="10"/>
            <path class="glyph-line" d="M8 18 H28 M10 13 H26 M10 23 H26"/>
          </svg>
          <span>www.qmpetrie.com</span>
        </li>
        <li class="contact-item">
          <svg class="contact-icon" viewBox="0 0 36 36" aria-hidden="true">
            <circle class="disc" cx="18" cy="18" r="18"/>
            <path class="glyph" d="M18 7 C12.8 7 9.5 10.8 9.5 15.3 C9.5 21 18 29.5 18 29.5 C18 29.5 26.5 21 26.5 15.3 C26.5 10.8 23.2 7 18 7 Z"/>
            <circle class="disc" cx="18" cy="15.3" r="3.4"/>
          </svg>
          <span>48, Linden Row, Harbor Lane, Country</span>
        </li>
      </ul>
    </section>
  </div>
</body>
</html>
```